We need a new design for our construction website

We need a new website for our wordpress site ferncrestworks.co.nz

It needs to be only a few pages but sleek in design and responsive, beautifully showcasing our images and video. Currently we have
1. home
2. about us
3. contact
We need either a front page that is designed much better to showcase more content, or potentially a projects page which has images from our builds. We don't have a lot of content so the content we do have needs to be maximised by image, rather than project.

Target Market(s)

High end residential construction and renovation projects, people wanting to build a nice home, clients based in Mount Maunganui, Tauranga.

Coding

Font styles to use
Sans Serif

Colors

Designer to choose only greyscale colors for use in the design.

Requirements
Must have
• A sleek design, architectural

```html
<!DOCTYPE html>
<html lang="en">
<head>
<meta charset="utf-8">
<title>Ferncrest — Home</title>
<link href="https://fonts.googleapis.com/css2?family=Poppins:wght@300;400;500;600&family=Anton&display=swap" rel="stylesheet">
<style>
:root{
  --black:#000;
  --ink:#111;
  --white:#fff;
  --grey-text:#555;
  --accent:#2b2b2b;
  --accent-soft:#8c8c8c;
  --muted:#bdbdbd;
  --band:rgba(30,30,30,.72);
}
*{margin:0;padding:0;box-sizing:border-box}
html,body{width:1200px;height:2651px;overflow:hidden;background:var(--white);font-family:'Poppins',sans-serif;color:var(--ink)}
.page{position:relative;width:1200px;height:2651px;overflow:hidden}
.abs{position:absolute}

/* header */
.site-header{left:0;top:0;width:1200px;height:89px;background:var(--black)}
.nav-link{top:37px;font-size:14px;color:var(--white);letter-spacing:.3px}
.nav-link.active{color:var(--accent-soft)}
.nav-link.active::after{content:"";position:absolute;left:-2px;right:-2px;bottom:-6px;height:2px;background:var(--accent-soft)}
.brand{font-size:22px;font-weight:400;letter-spacing:12px;color:var(--muted)}
.header-brand{left:492px;top:31px}
.search-icon{left:876px;top:36px}

/* hero */
.hero-photo{left:0;top:89px;width:1200px;height:588px;
  background:
    linear-gradient(100deg,rgba(0,0,0,0) 10%,rgba(40,40,40,.35) 25%,rgba(60,60,60,.25) 50%,rgba(0,0,0,0) 70%),
    linear-gradient(180deg,#b8b8b8 0%,#d6d6d6 35%,#8e8e8e 62%,#555 82%,#7a7a7a 100%)}
.hero-title{right:79px;top:262px;font-family:'Anton',sans-serif;font-size:53px;line-height:54px;text-align:right;color:var(--black);text-transform:uppercase}
.hero-band{left:669px;top:381px;width:531px;height:119px;background:var(--band)}
.hero-copy{right:79px;top:398px;width:440px;font-size:14.5px;line-height:27px;text-align:right;color:var(--white);font-weight:300}
.btn-solid{left:946px;top:512px;width:176px;height:53px;background:var(--accent);color:var(--white);font-size:18px;font-weight:500;display:flex;align-items:center;justify-content:center}
.slider-tab{left:519px;top:641px}

/* about */
.eyebrow{left:175px;top:752px;font-size:21px;font-weight:400}
.about-title{left:175px;top:780px;font-size:42px;font-weight:500;letter-spacing:.5px}
.about-text{left:177px;top:850px;width:430px;font-size:14.5px;line-height:27px;color:var(--grey-text);font-weight:300}
.about-text p+p{margin-top:14px}
.btn-outline{left:178px;top:1073px;width:188px;height:57px;border:1.5px solid var(--black);font-size:20px;font-weight:500;display:flex;align-items:center;justify-content:center}
.about-frame{left:804px;top:900px;width:261px;height:260px;border:6px solid var(--black);border-left:none;border-top:none}
.about-frame::before{content:"";position:absolute;right:-6px;top:0;width:40px;height:6px;background:var(--black)}
.about-photo{left:660px;top:750px;width:365px;height:375px;
  background:linear-gradient(165deg,#e4e4e4 0%,#cfcfcf 14%,#6e6e6e 30%,#4f4f4f 55%,#777 80%,#d9d9d9 100%)}

/* services */
.service{top:1229px;width:300px;height:365px;display:flex;align-items:flex-end;justify-content:center;padding-bottom:24px}
.service span{color:var(--white);font-size:20px;font-weight:500;line-height:25px;text-align:center}
.svc-1{left:0;background:linear-gradient(180deg,#a9a9a9 0%,#7c7c7c 45%,#3c3c3c 100%)}
.svc-2{left:300px;background:linear-gradient(180deg,#6a6a6a 0%,#b4b4b4 25%,#3e3e3e 55%,#7e7e7e 100%)}
.svc-3{left:600px;background:linear-gradient(180deg,#b0b0b0 0%,#7a7a7a 50%,#3a3a3a 100%)}
.svc-4{left:900px;background:linear-gradient(180deg,#e0e0e0 0%,#a6a6a6 55%,#5e5e5e 100%)}

/* testimonials */
.section-title{left:0;top:1660px;width:1200px;text-align:center;font-size:42px;font-weight:500;letter-spacing:1px}
.testimonial-photo{left:223px;top:1750px;width:437px;height:396px;background:linear-gradient(160deg,#5a5a5a 0%,#3a3a3a 50%,#8a8a8a 100%)}
.testimonial-card{left:532px;top:1920px;width:560px;height:260px;background:var(--white)}
.quote-mark{left:578px;top:1950px}
.quote-text{left:578px;top:1996px;width:500px;font-size:14.5px;line-height:27px;color:var(--grey-text);font-weight:300}
.quote-author{left:585px;top:2140px;font-size:20px;color:var(--accent);font-weight:400}

/* footer */
.site-footer{left:0;top:2339px;width:1200px;height:312px;background:var(--black)}
.cta-card{left:78px;top:2234px;width:402px;height:417px;background:linear-gradient(180deg,#4a4a4a,#333)}
.cta-title{left:122px;top:2286px;width:340px;font-size:23.5px;line-height:31px;font-weight:600;color:var(--white)}
.cta-text{left:122px;top:2396px;width:320px;font-size:14.5px;line-height:27px;color:#e6e6e6;font-weight:300}
.btn-ghost{left:125px;top:2530px;width:177px;height:52px;border:1.5px solid var(--white);color:var(--white);font-size:18px;font-weight:500;display:flex;align-items:center;justify-content:center}
.footer-heading{left:563px;top:2384px;font-size:15px;font-weight:500;color:var(--white);letter-spacing:.5px}
.sitemap{left:563px;top:2427px;list-style:none}
.sitemap li{position:relative;padding-left:25px;font-size:14.5px;color:#ddd;line-height:31px;font-weight:300}
.sitemap li::before{content:"";position:absolute;left:0;top:13px;width:6px;height:6px;border-radius:50%;background:var(--accent-soft)}
.footer-brand{left:885px;top:2386px;color:var(--white)}
.contact-line{left:833px;font-size:14.5px;color:#ccc;font-weight:300;display:flex;align-items:center;gap:17px}
.social-dot{left:830px;top:2512px;width:42px;height:42px;border-radius:50%;background:#555}
.footer-rule{left:480px;top:2589px;width:720px;height:1px;background:#222}
.copyright{left:563px;top:2609px;font-size:14px;color:#bbb;font-weight:300}
.copyright span{color:var(--white)}
</style>
</head>
<body>
<div class="page">

  <header class="abs site-header">
    <span class="abs nav-link active" style="left:310px">HOME</span>
    <span class="abs nav-link" style="left:379px">ABOUT</span>
    <span class="abs brand header-brand">FERNCREST</span>
    <span class="abs nav-link" style="left:776px">CONTACT</span>
    <svg class="abs search-icon" width="18" height="18" viewBox="0 0 18 18" fill="none" stroke="#fff" stroke-width="2"><circle cx="7" cy="7" r="5"/><path d="M11 11l5 5"/></svg>
  </header>

  <section>
    <div class="abs hero-photo" role="img" aria-label="Modern glass office building with landscaped street and pedestrians"></div>
    <h1 class="abs hero-title">We build your<br>dream home</h1>
    <div class="abs hero-band"></div>
    <p class="abs hero-copy">Our vision is to build beautiful, efficient homes with the<br>best building technologies available that our<br>customers are proud to own.</p>
    <a class="abs btn-solid">GET STARTED</a>
    <svg class="abs slider-tab" width="162" height="36" viewBox="0 0 162 36">
      <path d="M22 0H140L162 36H0Z" fill="#2b2b2b"/>
      <g fill="none" stroke="#fff" stroke-width="1.3"><circle cx="49" cy="18" r="5"/><circle cx="70" cy="18" r="5"/><circle cx="113" cy="18" r="5"/></g>
      <circle cx="92" cy="18" r="6" fill="#fff"/>
    </svg>
  </section>

  <section>
    <div class="abs eyebrow">ABOUT</div>
    <h2 class="abs about-title">FERNCREST</h2>
    <div class="abs about-text">
      <p>Kauri Ridge Homes Ltd T/A Ferncrest was founded in 1985<br>by Graham Whitfield and began trading as Ferncrest in<br>2017 with sons Sam and Leo at the helm.</p>
      <p>With the company’s roots previously in solid timber, the<br>team have a special interest in architectural homes,<br>alternative building technologies and sustainable<br>building practices.</p>
    </div>
    <a class="abs btn-outline">LEARN MORE</a>
    <div class="abs about-frame"></div>
    <div class="abs about-photo" role="img" aria-label="Brick heritage building with stone trim against the sky"></div>
  </section>

  <section>
    <div class="abs service svc-1" role="img" aria-label="Engineer in hard hat holding a tablet on a building site"><span>Design And<br>Build</span></div>
    <div class="abs service svc-2" role="img" aria-label="Renovated modern bathroom with walk-in shower"><span>Renovations &amp;<br>Additions</span></div>
    <div class="abs service svc-3" role="img" aria-label="Glass tower under construction beside a crane"><span>Build<br>Smarter</span></div>
    <div class="abs service svc-4" role="img" aria-label="Two project managers reviewing plans at a laptop"><span>Project<br>Management</span></div>
  </section>

  <section>
    <h2 class="abs section-title">TESTIMONIALS</h2>
    <div class="abs testimonial-photo" role="img" aria-label="Happy homeowner standing in front of an apartment building"></div>
    <div class="abs testimonial-card"></div>
    <svg class="abs quote-mark" width="36" height="32" viewBox="0 0 36 32" fill="#000">
      <path d="M0 32V16L8 0h7L10 14h6v18zM20 32V16L28 0h7l-5 14h6v18z"/>
    </svg>
    <p class="abs quote-text">Our home is the envy of many friends. It holds the warmth<br>incredibly through the winter and is perfectly cool in the summer.<br>The ease of design has made it not only very smart with a<br>modern feel but also with its strong robust construction it feels<br>safe and secure for our young family. We love our home!</p>
    <div class="abs quote-author">— Helena</div>
  </section>

  <footer>
    <div class="abs site-footer"></div>
    <div class="abs cta-card"></div>
    <h3 class="abs cta-title">Contact us For a Free no<br>Obligation Chat About<br>Your Building Project</h3>
    <p class="abs cta-text">We’d love to hear about your building project and discuss how Ferncrest can help you design and build your dream home smarter.</p>
    <a class="abs btn-ghost">GET IN TOUCH</a>

    <div class="abs footer-heading">SITEMAP</div>
    <ul class="abs sitemap"><li>Home</li><li>About Us</li><li>Contact Us</li></ul>

    <span class="abs brand footer-brand" style="color:#fff;font-size:21px">FERNCREST</span>
    <div class="abs contact-line" style="top:2440px">
      <svg width="18" height="18" viewBox="0 0 24 24" fill="#8c8c8c"><path d="M6.6 10.8a15 15 0 006.6 6.6l2.2-2.2a1 1 0 011-.25 11.4 11.4 0 003.6.6 1 1 0 011 1V20a1 1 0 01-1 1A17 17 0 013 4a1 1 0 011-1h3.5a1 1 0 011 1 11.4 11.4 0 00.6 3.6 1 1 0 01-.25 1z"/></svg>
      <span>0275550142</span>
    </div>
    <div class="abs contact-line" style="top:2476px">
      <svg width="19" height="14" viewBox="0 0 20 14"><rect width="20" height="14" fill="#8c8c8c"/><path d="M0 0l10 7 10-7" fill="none" stroke="#000" stroke-width="1.5"/></svg>
      <span>admin@ferncrestworks.co.nz</span>
    </div>
    <div class="abs social-dot" aria-label="Social media link"></div>
    <div class="abs footer-rule"></div>
    <p class="abs copyright">©<span>FERNCREST</span> -2020 All rights reserved.</p>
  </footer>

</div>
</body>
</html>
```